Tobias Wrenfield - Cinematographer

NEED:
I'm looking for a sleek, professional, modern business card that will give give the recipient the impression that they can trust their production will go smoothly by hiring me. I will bring creativity and knowledge to their shoot, so that we can create powerful images.
I am looking for a card with a strong style and design ethos that could be expanded to a website and a full visual/graphic/design entity for me.
ABOUT ME:
I am a mid-twenties cinematographer, I work on music video, narrative short, commercial, and corporate projects. I blend the science and artistry of cameras and filmmaking to tell a story. I'm an artist, a technician, and a manager.
DESIGN:
I like sleek, simple design. Black, dark grays, white, dark navy, steel blues, I love cyan, but also cyan and red. I am not a fan of earthy tones. I generally prefer modern, san-serif fonts over serifs. My old logo was based on an aperture, a multi-blade device at the back of a lens that controls how much light passes through, but I made it with so many colors, that it doesn't necessarily lend itself to a specific color-scheme or design ethos. I liked that the aperture design provided a sense of the technical requirements of my job. I'm a fan of matte business cards, but am open to plenty of specialty print processes to make an outstanding card.
ATTACHED FILES:
My Old Rainbox Aperture Logo, plus a few designs I've tried playing around with, but am not tied to. I AM OPEN TO NEW DESIGNS, DO NOT FEEL TIED TO THIS.
**I've pulled my old logo down from the attached files, and instead attached other business cards I like, so as not to mislead you where I would like to go.
INFO:
Name: Tobias Wrenfield
Job: Cinematographer
Email: tkwrenfield@quillbox.example
Phone: 503.618.2907
Website: tobiaswrenfield.example
Updates
I'm adding some images of other cards that I like, and removing my old logo, since I'm looking for something new, and don't want that old logo to push anyone a certain direction.

```html
<!DOCTYPE html>
<html lang="en">
<head>
<meta charset="utf-8">
<title>Tobias Wrenfield – Cinematographer Business Card</title>
<link rel="stylesheet" href="https://fonts.googleapis.com/css2?family=Oswald:wght@300;400&display=swap">
<style>
  :root {
    --stage: #555555;
    --card-edge: #777777;
    --black: #000000;
    --slate: #565656;
    --charcoal: #3b3b3b;
    --rule: #cccccc;
    --white: #ffffff;
    --ink: #111111;
    --muted: #9a9a9a;
  }
  html, body {
    margin: 0;
    padding: 0;
    width: 1200px;
    height: 407px;
    overflow: hidden;
    background: var(--stage);
  }
  .stage {
    position: relative;
    width: 1200px;
    height: 407px;
    font-family: "Oswald", "Arial Narrow", sans-serif;
  }
  .card {
    position: absolute;
    top: 13px;
    width: 578px;
    height: 384px;
    overflow: hidden;
    box-shadow: 0 0 0 1px var(--card-edge);
  }
  .card--back { left: 13px; }
  .card--front { left: 607px; background: var(--white); }
  .card__art {
    position: absolute;
    inset: 0;
    width: 578px;
    height: 384px;
  }
  .seal__name {
    position: absolute;
    left: 381px;
    top: 156px;
    width: 160px;
    margin: 0;
    font-weight: 300;
    font-size: 28px;
    line-height: 32px;
    text-align: center;
    letter-spacing: 0.5px;
  }
  .seal__name--back { color: var(--white); }
  .seal__name--front { color: var(--rule); }
  .front__name {
    position: absolute;
    left: 12px;
    top: 109px;
    margin: 0;
    font-weight: 300;
    font-size: 64px;
    line-height: 1;
    letter-spacing: -0.5px;
    color: var(--ink);
    white-space: nowrap;
  }
  .front__role {
    position: absolute;
    right: 217px;
    top: 192px;
    margin: 0;
    font-weight: 300;
    font-size: 25px;
    line-height: 1;
    color: var(--muted);
    white-space: nowrap;
  }
  .front__contact {
    position: absolute;
    left: 18px;
    top: 304px;
    margin: 0;
    font-weight: 300;
    font-size: 14px;
    line-height: 21px;
    color: var(--ink);
    font-style: normal;
  }
</style>
</head>
<body>
<main class="stage">

  <section class="card card--back" aria-label="Card back">
    <svg class="card__art" viewBox="0 0 578 384" aria-hidden="true">
      <rect class="panel-top-left" x="0" y="0" width="461" height="188" fill="var(--black)"/>
      <rect class="panel-top-right" x="461" y="0" width="117" height="188" fill="var(--slate)"/>
      <rect class="panel-bottom-left" x="0" y="188" width="461" height="196" fill="var(--charcoal)"/>
      <rect class="panel-bottom-right" x="461" y="188" width="117" height="196" fill="var(--black)"/>
      <line x1="461" y1="0" x2="461" y2="384" stroke="var(--rule)" stroke-width="4"/>
      <line x1="0" y1="188" x2="578" y2="188" stroke="var(--rule)" stroke-width="4"/>
      <circle class="seal" cx="461" cy="188" r="85" fill="var(--black)" stroke="var(--rule)" stroke-width="5"/>
    </svg>
    <p class="seal__name seal__name--back">Tobias<br>Wrenfield</p>
  </section>

  <section class="card card--front" aria-label="Card front">
    <svg class="card__art" viewBox="0 0 578 384" aria-hidden="true">
      <line x1="463" y1="0" x2="463" y2="384" stroke="var(--rule)" stroke-width="4"/>
      <line x1="0" y1="188" x2="578" y2="188" stroke="var(--rule)" stroke-width="4"/>
      <circle class="seal" cx="463" cy="188" r="85" fill="var(--white)" stroke="var(--rule)" stroke-width="4"/>
    </svg>
    <p class="seal__name seal__name--front" style="left:383px">Tobias<br>Wrenfield</p>
    <h1 class="front__name">Tobias Wrenfield</h1>
    <p class="front__role">Cinematographer</p>
    <address class="front__contact">
      Email: tkwrenfield@quillbox.example<br>
      Phone: 503.618.2907<br>
      Website: tobiaswrenfield.example
    </address>
  </section>

</main>
</body>
</html>
```